Letterhead for New Orthopaedic Surgery Practice

My husband and I are starting our own practice named RB Spine & Vitality Center. We would like to create a nice simple but high class letterhead that doesn't use too much solid color ink when printing. I like the colors dark blue, gold, yellow. Open to other suggestions. We will need to list him and I both on the top of the letterhead. Here is the important information:
Abena Quist, M.D. - Hand and Upper Extremity Surgery
Abena Quist, M.D. - Hip & Knee Replacement/General Orthopaedic Surgery
Location: 18735 North Harlow Pkwy
Brightmoor Bay, FL 33099
Phone: 954-218-4650
Fax: 954-582-1346
Email: info@myrbspine.com

The only thing is that the phone and fax numbers will change once we get into our space. I just want to get the design started. I am including several documents which are my previous practice letterhead, my current procedure room letterhead, and our new Logo. The other letterheads are just for examples but please think outside of the box! We would love to see some great designs.

Colors
0054AA
0677BA
7BADD7
CADEEF
E8F1F8
0094D4
00A9DD
6FCCEA
C7EBF8
E9F6FB

Requirements
Must have
• class, elegance, luxury

```html
<!DOCTYPE html>
<html lang="en">
<head>
<meta charset="utf-8">
<title>RB Spine &amp; Vitality Center — Letterhead</title>
<link href="https://fonts.googleapis.com/css2?family=Montserrat:wght@400;500;700&display=swap" rel="stylesheet">
<style>
  :root {
    --navy: #1b2a52;
    --gold: #c6a25e;
    --ink: #2a2a2a;
    --paper: #ffffff;
    --backdrop: #e9eaec;
  }
  * { box-sizing: border-box; margin: 0; padding: 0; }
  html, body {
    width: 1200px; height: 874px; overflow: hidden;
    background: var(--backdrop);
    font-family: "Montserrat", Arial, sans-serif;
  }
  .letterhead {
    position: absolute; left: 310px; top: 27px;
    width: 580px; height: 820px;
    background: var(--paper);
    box-shadow: 0 2px 10px rgba(0,0,0,.12);
    overflow: hidden;
    color: var(--ink);
  }
  .brand {
    position: absolute; left: 38px; top: 38px;
    display: flex; align-items: center; gap: 8px;
  }
  .brand-dot {
    width: 14px; height: 14px; border-radius: 50%;
    background: var(--gold);
  }
  .brand-name {
    font-size: 11px; font-weight: 700; color: var(--navy);
    letter-spacing: .08em; text-transform: uppercase;
    line-height: 1.35; width: 120px;
  }
  .physicians {
    position: absolute; right: 200px; top: 40px;
    text-align: right; padding-right: 12px;
    border-right: 1px solid var(--gold);
  }
  .physician-name {
    font-size: 11.5px; font-weight: 700; color: var(--navy);
    letter-spacing: .02em;
  }
  .physician-specialty {
    font-size: 7.5px; color: var(--ink); margin-bottom: 5px; line-height: 1.3;
  }
  .contact {
    position: absolute; left: 392px; top: 38px;
    font-size: 7.5px; line-height: 1.55; color: var(--ink);
    font-style: normal;
  }
  .contact-line { display: flex; align-items: center; gap: 4px; }
  .contact-line svg { width: 7px; height: 7px; fill: var(--gold); }
  .contact-address { margin-bottom: 3px; }
  .recipient {
    position: absolute; left: 56px; top: 205px;
    font-size: 8.5px; line-height: 1.6;
  }
  .body-text {
    position: absolute; left: 56px; top: 275px; width: 410px;
    font-size: 8.5px; line-height: 1.6;
  }
  .body-text p { margin-bottom: 12px; }
  .closing {
    position: absolute; left: 56px; top: 520px;
    font-size: 8.5px;
  }
  .signature-area {
    position: absolute; left: 56px; top: 542px;
    width: 120px; height: 34px;
    background: linear-gradient(90deg, #f0f0f0, #e4e4e4);
  }
  .corner-swoosh {
    position: absolute; left: 0; top: 0; width: 580px; height: 820px;
  }
</style>
</head>
<body>
  <main class="letterhead">
    <svg class="corner-swoosh" viewBox="0 0 580 820" aria-hidden="true">
      <path d="M580 360 C 562 590 380 760 150 820" fill="none" stroke="var(--gold)" stroke-width="7"/>
      <path d="M580 380 C 566 600 400 770 196 820 L580 820 Z" fill="var(--navy)"/>
    </svg>

    <header>
      <div class="brand">
        <span class="brand-dot"></span>
        <span class="brand-name">RB Spine &amp; Vitality Center</span>
      </div>

      <div class="physicians">
        <div class="physician-name">LUCINDA PERROW, M.D.</div>
        <div class="physician-specialty">Hand and Upper Extremity Surgery</div>
        <div class="physician-name">ABENA QUIST, M.D.</div>
        <div class="physician-specialty">Hip &amp; Knee Replacement/General<br>Orthopaedic Surgery</div>
      </div>

      <address class="contact">
        <div class="contact-address">18735 North Harlow Pkwy<br>Brightmoor Bay, FL 33099</div>
        <div class="contact-line"><svg viewBox="0 0 10 10"><path d="M2 0 L4 2 L3 3.5 Q4.5 6 6.5 7 L8 6 L10 8 L8.5 10 Q1 8 0 1.5Z"/></svg>954-218-4650</div>
        <div class="contact-line"><svg viewBox="0 0 10 10"><rect x="1" y="3" width="8" height="5" rx="1"/><rect x="3" y="0" width="4" height="3"/></svg>954-582-1346</div>
        <div class="contact-line"><svg viewBox="0 0 10 10"><rect x="0" y="2" width="10" height="6" rx="1"/></svg>info@myrbspine.com</div>
      </address>
    </header>

    <section class="recipient">
      Mr/s<br>First Name and Last Name<br>Company Name<br>Address
    </section>

    <section class="body-text">
      <p>Lorem Ipsum is simply dummy text of the printing and typesetting industry. Lorem Ipsum has been the industry's standard dummy text ever since the 1500s, when an unknown printer took a galley of type and scrambled it to make a type specimen book. It has survived not only five centuries, but also the leap into electronic typesetting, remaining essentially unchanged. It was popularised in the 1960s.</p>
      <p>The standard chunk of Lorem Ipsum used since the 1500s is reproduced below for those interested. Sections 1.10.32 and 1.10.33 from "de Ordine Verborum" by Tellanus are also reproduced in their exact original form, accompanied by English versions from the 1914 translation by H. Orrinford. Lorem ipsum dolor sit amet, consectetur adipiscing elit, sed do eiusmod tempor incididunt ut labore et dolore magna aliqua.</p>
      <p>It is a long established fact that a reader will be distracted by the readable content of a page when looking at its layout. The point of using Lorem Ipsum is that it has a more-or-less normal distribution of letters, as opposed to using 'Content here, content here', making it look like readable English. Many desktop publishing packages and web page editors now.</p>
    </section>

    <div class="closing">Your Sincerely,</div>
    <div class="signature-area" role="img" aria-label="Handwritten signature"></div>
  </main>
</body>
</html>
```